Consulting firm need a professional powerpoint design

A startup Climate change firm needs a powerpoint template design. The design should reflect aspects of climate change adaptation, resilience and environmental sustainability.

The powerpoint design must convey aspects of nature and climate action for a resilient society.

The last slide of the powerpoint must have a allocation for a slogan such as 'Bridging evidence and policy action'.

Use the colors in the logo and business card for the powerpoint design.

Target Market(s)

Government and industry

Font styles to use
Sans Serif
Other font styles liked:
• nexa font family

Colors
85cae6
abd037
fece3e

Requirements
Must have
• - Colors used in logo and business card
- Convey science and nature
- Professional
Nice to have
• Many pages
Should not have
• Not complicated

```html
<!DOCTYPE html>
<html lang="en">
<head>
<meta charset="utf-8">
<title>Terravera Presentation Template</title>
<link rel="stylesheet" href="https://fonts.googleapis.com/css2?family=Poppins:wght@300;400;500;600;700;800&display=swap">
<style>
:root{
  --stage:#323c4f;
  --white:#ffffff;
  --navy:#2c3350;
  --ink:#3a3f4b;
  --muted:#6b7080;
  --cyan:#1ba0d8;
  --blue:#0b6cc0;
  --sky:#85cae6;
  --lime:#abd037;
  --green:#8cc63f;
  --sun:#fece3e;
  --teal:#1fc3ad;
  --mist:#dfeaf6;
  --panel:#f1f1f1;
  --rule:#d9d9d9;
}
*{box-sizing:border-box;margin:0;padding:0}
html,body{width:1200px;height:2700px;overflow:hidden}
body{background:var(--stage);font-family:"Poppins",sans-serif;color:var(--ink);position:relative}
.slide{position:absolute;background:var(--white);overflow:hidden;box-shadow:0 10px 24px rgba(0,0,0,.28)}
.slide--small{width:492px;height:274px}
.abs{position:absolute}

/* brand */
.brand{position:absolute;display:flex;align-items:center;gap:4px;color:var(--navy);font-weight:600;letter-spacing:.5px}
.brand__dot{width:9px;height:9px;border-radius:50%;background:var(--teal)}
.slide--small .brand{top:18px;right:20px;font-size:7px}

/* small slide header */
.section-label{position:absolute;left:26px;top:16px;font-size:8px;color:var(--cyan);font-weight:400;letter-spacing:.2px}
.slide-title{position:absolute;left:26px;top:28px;font-size:15px;font-weight:700;color:var(--navy);letter-spacing:-.2px}
.title-rule{position:absolute;left:26px;top:54px;width:54px;height:1px;background:#aab0bb}
.copy{font-size:6.8px;line-height:1.3;color:var(--ink)}
.kicker{font-size:8.5px;font-weight:700;color:var(--cyan)}
.placeholder{position:absolute}

/* hero */
.hero{left:95px;top:244px;width:1017px;height:572px}
.hero .brand{left:601px;top:100px;flex-direction:column;align-items:flex-start;gap:0}
.hero__name{display:flex;align-items:center;gap:10px;font-size:30px;font-weight:600;color:var(--navy);letter-spacing:2px}
.hero__name .brand__dot{width:40px;height:40px}
.hero__tag{font-size:12.5px;color:var(--navy);font-weight:400;margin-left:50px;margin-top:-6px}
.hero__title{position:absolute;left:601px;top:210px;font-size:42px;line-height:51px;font-weight:800;color:var(--navy);letter-spacing:.5px}
.hero__rule{position:absolute;left:601px;top:378px;width:100px;height:3px;background:var(--sun)}
.hero__subtitle{position:absolute;left:601px;top:396px;font-size:18px;font-weight:300;color:var(--cyan)}
.hero__art{left:118px;top:82px;width:420px;height:400px;border-radius:50%;background:radial-gradient(circle at 50% 35%,#fde66c 0%,#f6d84a 28%,#9ccb55 55%,#5fae6a 80%,#cfe7a0 100%)}

/* compare */
.compare{left:95px;top:889px}
.compare__half{position:absolute;left:252px;top:0;width:240px;height:274px;background:var(--mist)}
.compare__left{position:absolute;left:26px;top:94px;width:128px}
.compare__right{position:absolute;left:340px;top:94px;width:130px;text-align:right}
.compare__art{left:172px;top:88px;width:142px;height:145px;border-radius:50%;background:radial-gradient(circle,#3c8fd6 0%,#4aa85a 50%,#f0c24a 78%,#e6e6e6 100%)}

/* three points */
.three{left:95px;top:1237px}
.card{position:absolute;top:80px;width:130px;height:166px;background:var(--panel);text-align:center;padding:0 10px}
.card__icon{margin:12px auto 0;width:44px;height:44px;border-radius:6px;background:linear-gradient(135deg,#3b8fd1,#ffd34d)}
.card__title{margin-top:14px;font-size:9px;font-weight:700;color:var(--navy)}
.card .copy{margin-top:6px;color:var(--muted)}
.card__bar{position:absolute;left:0;bottom:0;width:100%;height:5px}

/* body text */
.bodytext{left:95px;top:1585px}
.bodytext__copy{position:absolute;left:28px;top:82px;width:242px}
.bodytext__copy p+p{margin-top:7px}
.bodytext__art{left:318px;top:52px;width:120px;height:150px;border-radius:40% 40% 10% 10%;background:linear-gradient(180deg,#ffd84a,#f3b82a 60%,#3a8d4a)}

/* pie */
.pie{left:95px;top:1934px}
.pie__box{position:absolute;left:25px;top:80px;width:230px;height:165px;background:var(--panel)}
.pie__legend{position:absolute;left:176px;top:62px;font-size:5.5px;color:var(--muted);line-height:12px}
.pie__legend i{display:inline-block;width:4px;height:4px;margin-right:3px}
.stat{position:absolute;left:283px;display:flex;align-items:center;gap:12px}
.stat__dot{width:28px;height:28px;border-radius:50%;border:3px solid #e6e9ef;display:flex;align-items:center;justify-content:center;font-size:8px;font-weight:700;color:var(--white)}
.stat .copy{width:135px}

/* agenda */
.agenda{left:621px;top:1080px}
.agenda__item{position:absolute;display:flex;gap:10px;align-items:center}
.agenda__num{width:30px;height:30px;border-radius:50%;border:3px solid #e8ecf1;display:flex;align-items:center;justify-content:center;color:var(--white);font-size:10px;font-weight:700;flex:none}
.agenda__head{font-size:7.5px;font-weight:700;color:var(--navy)}
.agenda__item .copy{width:140px}

/* four points */
.four{left:621px;top:1419px}
.point{position:absolute;width:208px;height:84px;border:1px solid #dcdcdc;border-radius:10px;padding:10px 20px}
.point--right{text-align:right}
.point .kicker{display:block;margin-bottom:6px}
.point .copy{color:var(--muted)}
.four__hub{position:absolute;left:193px;top:118px;width:106px;height:106px;border-radius:50%;background:var(--white);border:1px solid #dcdcdc;display:flex;align-items:center;justify-content:center}
.four__hub span{width:60px;height:60px;border-radius:50%;background:var(--sky)}

/* table */
.tablesl{left:621px;top:1757px}
.data{position:absolute;left:25px;top:75px;width:441px;border-collapse:collapse;font-size:6px;color:var(--ink)}
.data th{height:17px;color:var(--white);font-weight:600;font-size:6.5px}
.data td{height:16px;border-bottom:1px solid #e2e2e2;text-align:center}
.data td:first-child{text-align:left;padding-left:10px}
.data tr:nth-child(even) td{background:#f6f6f6}
.data td+td{border-left:1px solid #e2e2e2}

/* timeline */
.timeline{left:621px;top:2095px}
.tl__line{position:absolute;left:20px;top:165px;width:452px;height:2px;background:#c9c9c9}
.tl__end{position:absolute;top:162px;width:8px;height:8px;border-radius:50%;background:#b5b5b5}
.tl__node{position:absolute;top:154px;width:24px;height:24px;border-radius:50%;border:3px solid #e6e9ef;color:var(--white);font-size:9px;font-weight:700;display:flex;align-items:center;justify-content:center}
.tl__stem{position:absolute;width:1px;background:#9a9a9a}
.tl__note{position:absolute;width:58px}
</style>
</head>
<body>

<!-- Title slide -->
<section class="slide hero">
  <svg class="abs" style="left:0;top:0" width="1017" height="572" viewBox="0 0 1017 572">
    <path d="M0 240 C60 190 150 200 170 260 C185 300 150 330 190 360 L0 380 Z" fill="#e1f1f8"/>
    <path d="M0 300 C40 290 90 310 110 340 C130 380 90 410 160 430 C260 460 330 420 420 410 C520 400 620 430 690 572 L0 572 Z" fill="var(--teal)"/>
    <ellipse cx="330" cy="500" rx="90" ry="8" fill="#5fd8c6"/>
  </svg>
  <div class="placeholder hero__art" role="img" aria-label="Illustration of a green globe topped by hills, trees, wind turbines and solar panels under a bright sun"></div>
  <div class="brand">
    <div class="hero__name"><span class="brand__dot"></span>TERRAVERA</div>
    <div class="hero__tag">Bridging evidence and policy action</div>
  </div>
  <h1 class="hero__title">YOUR<br>PRESENTATION<br>GOES HERE</h1>
  <div class="hero__rule"></div>
  <p class="hero__subtitle">YOUR SUBTITLE GOES HERE</p>
</section>

<!-- Compare -->
<section class="slide slide--small compare">
  <div class="compare__half"></div>
  <p class="section-label">SECTION NAME HERE</p>
  <h2 class="slide-title">COMPARE SLIDE GOES HERE</h2>
  <div class="title-rule"></div>
  <div class="brand"><span class="brand__dot"></span>TERRAVERA</div>
  <div class="compare__left">
    <p class="kicker" style="margin-bottom:8px">Lorem ipsum</p>
    <p class="copy">It is a long established fact that a reader will be distracted by the readable content of a page when looking at its layout. The point of using Lorem Ipsum is that it has a more-or-less normal distribution of letters, as opposed to using 'Content here, content here', making it look like readable English. Many desktop publishing packages and web page editors now use Lorem Ipsum as their default model text, and a search for 'lorem ipsum' will uncover many web sites still in their infancy.</p>
  </div>
  <div class="placeholder compare__art" role="img" aria-label="Illustration of the Earth surrounded by city buildings and smoking factories"></div>
  <div class="compare__right">
    <p class="kicker" style="margin-bottom:8px">Lorem ipsum</p>
    <p class="copy">There are many variations of passages of Lorem Ipsum available, but the majority have suffered alteration in some form, by injected humour, or randomised words which don't look even slightly believable. If you are going to use a passage of Lorem Ipsum, you need to be sure there isn't anything embarrassing hidden in the middle of text. All the Lorem Ipsum generators on the Internet tend to repeat predefined chunks as necessary, making this the first true generator on the Internet.</p>
  </div>
</section>

<!-- Three points -->
<section class="slide slide--small three">
  <p class="section-label">SECTION NAME HERE</p>
  <h2 class="slide-title">THREE POINTS SLIDE GOES HERE</h2>
  <div class="title-rule"></div>
  <div class="brand"><span class="brand__dot"></span>TERRAVERA</div>
  <div class="card" style="left:30px">
    <div class="card__icon" role="img" aria-label="Icon of an ocean buoy on waves"></div>
    <p class="card__title">Lorem ipsum</p>
    <p class="copy">Lorem Ipsum is simply dummy text of the printing and typesetting industry. Lorem Ipsum has been the industry's standard dummy text ever since the 1500s</p>
    <div class="card__bar" style="background:var(--sun)"></div>
  </div>
  <div class="card" style="left:180px">
    <div class="card__icon" role="img" aria-label="Icon of a raised fist holding the globe"></div>
    <p class="card__title">Lorem ipsum</p>
    <p class="copy">Lorem Ipsum is simply dummy text of the printing and typesetting industry. Lorem Ipsum has been the industry's standard dummy text ever since the 1500s</p>
    <div class="card__bar" style="background:var(--sky)"></div>
  </div>
  <div class="card" style="left:330px">
    <div class="card__icon" role="img" aria-label="Icon of a globe with sprouting plants"></div>
    <p class="card__title">Lorem ipsum</p>
    <p class="copy">Lorem Ipsum is simply dummy text of the printing and typesetting industry. Lorem Ipsum has been the industry's standard dummy text ever since the 1500s</p>
    <div class="card__bar" style="background:var(--green)"></div>
  </div>
</section>

<!-- Body text -->
<section class="slide slide--small bodytext">
  <p class="section-label">SECTION NAME HERE</p>
  <h2 class="slide-title">BODY TEXT SLIDE GOES HERE</h2>
  <div class="title-rule"></div>
  <div class="brand"><span class="brand__dot"></span>TERRAVERA</div>
  <div class="bodytext__copy copy">
    <p>Contrary to popular belief, Lorem Ipsum is not simply random text. It has roots in a piece of classical Latin literature from 45 BC, making it over 2000 years old. A Latin scholar at a small college looked up one of the more obscure Latin words, consectetur, from a Lorem Ipsum passage, and going through the cites of the word in classical literature, discovered the undoubtable source. Lorem Ipsum comes from sections 1.10.32 and 1.10.33 of an ancient work on the extremes of good and evil, written in 45 BC by an ancient author. This book is a treatise on the theory of ethics, very popular during the Renaissance. The first line of Lorem Ipsum, "Lorem ipsum dolor sit amet..", comes from a line in section 1.10.32.</p>
    <p>The standard chunk of Lorem Ipsum used since the 1500s is reproduced below for those interested. Sections 1.10.32 and 1.10.33 from that same ancient treatise are also reproduced in their exact original form, accompanied by English versions from a later translation by a noted scholar.</p>
  </div>
  <svg class="abs" style="left:0;top:0" width="492" height="274" viewBox="0 0 492 274">
    <path d="M280 274 C300 215 360 190 420 185 C455 182 480 170 492 150 L492 274 Z" fill="#c6e07a"/>
    <path d="M330 274 C350 240 400 225 450 222 C470 221 485 214 492 205 L492 274 Z" fill="var(--lime)"/>
  </svg>
  <div class="placeholder bodytext__art" role="img" aria-label="Illustration of a glowing light bulb containing the globe, growing on a plant stem"></div>
</section>

<!-- Pie chart -->
<section class="slide slide--small pie">
  <p class="section-label">SECTION NAME HERE</p>
  <h2 class="slide-title">PIE CHART GOES TEXT HERE</h2>
  <div class="title-rule"></div>
  <div class="brand"><span class="brand__dot"></span>TERRAVERA</div>
  <div class="pie__box">
    <svg class="abs" style="left:20px;top:12px" width="140" height="140" viewBox="-70 -70 140 140" font-family="Poppins, sans-serif" font-size="10" font-weight="700" fill="#fff" text-anchor="middle">
      <g transform="rotate(-90)" fill="none" stroke-width="24">
        <circle r="54" stroke="var(--blue)" stroke-dasharray="199.5 339.3"/>
        <circle r="54" stroke="var(--lime)" stroke-dasharray="77.6 339.3" stroke-dashoffset="-199.5"/>
        <circle r="54" stroke="var(--sun)" stroke-dasharray="33.9 339.3" stroke-dashoffset="-277.1"/>
        <circle r="54" stroke="var(--sky)" stroke-dasharray="29.1 339.3" stroke-dashoffset="-311"/>
      </g>
      <text x="53" y="16">8.2</text>
      <text x="-53" y="16">3.2</text>
      <text x="-40" y="-30">1.4</text>
      <text x="-13" y="-50">1.2</text>
    </svg>
    <div class="pie__legend">
      <div><i style="background:var(--blue)"></i>1st Qtr</div>
      <div><i style="background:var(--lime)"></i>2nd Qtr</div>
      <div><i style="background:var(--sun)"></i>3rd Qtr</div>
      <div><i style="background:var(--sky)"></i>4th Qtr</div>
    </div>
  </div>
  <div class="stat" style="top:84px"><span class="stat__dot" style="background:var(--blue)">8.2</span><p class="copy">Lorem Ipsum is simply dummy text of the printing and typesetting industry.</p></div>
  <div class="stat" style="top:126px"><span class="stat__dot" style="background:var(--sky)">1.2</span><p class="copy">Lorem Ipsum is simply dummy text of the printing and typesetting industry.</p></div>
  <div class="stat" style="top:167px"><span class="stat__dot" style="background:var(--lime)">3.2</span><p class="copy">Lorem Ipsum is simply dummy text of the printing and typesetting industry.</p></div>
  <div class="stat" style="top:209px"><span class="stat__dot" style="background:var(--sun)">1.4</span><p class="copy">Lorem Ipsum is simply dummy text of the printing and typesetting industry.</p></div>
</section>

<!-- Agenda -->
<section class="slide slide--small agenda">
  <p class="section-label">SECTION NAME HERE</p>
  <h2 class="slide-title">AGENDA SLIDE GOES HERE</h2>
  <div class="title-rule"></div>
  <div class="brand"><span class="brand__dot"></span>TERRAVERA</div>
  <div class="agenda__item" style="left:35px;top:82px"><span class="agenda__num" style="background:var(--sun)">01</span><div><p class="agenda__head">Heading here</p><p class="copy">Lorem Ipsum is simply dummy text of the printing and typesetting industry.</p></div></div>
  <div class="agenda__item" style="left:35px;top:147px"><span class="agenda__num" style="background:var(--lime)">02</span><div><p class="agenda__head">Heading here</p><p class="copy">Lorem Ipsum is simply dummy text of the printing and typesetting industry.</p></div></div>
  <div class="agenda__item" style="left:35px;top:212px"><span class="agenda__num" style="background:var(--sky)">03</span><div><p class="agenda__head">Heading here</p><p class="copy">Lorem Ipsum is simply dummy text of the printing and typesetting industry.</p></div></div>
  <div class="agenda__item" style="left:262px;top:82px"><span class="agenda__num" style="background:var(--sun)">04</span><div><p class="agenda__head">Heading here</p><p class="copy">Lorem Ipsum is simply dummy text of the printing and typesetting industry.</p></div></div>
  <div class="agenda__item" style="left:262px;top:147px"><span class="agenda__num" style="background:var(--lime)">05</span><div><p class="agenda__head">Heading here</p><p class="copy">Lorem Ipsum is simply dummy text of the printing and typesetting industry.</p></div></div>
  <div class="agenda__item" style="left:262px;top:212px"><span class="agenda__num" style="background:var(--sky)">06</span><div><p class="agenda__head">Heading here</p><p class="copy">Lorem Ipsum is simply dummy text of the printing and typesetting industry.</p></div></div>
</section>

<!-- Four points -->
<section class="slide slide--small four">
  <p class="section-label">SECTION NAME HERE</p>
  <h2 class="slide-title">FOUR POINTS SLIDE GOES HERE</h2>
  <div class="title-rule"></div>
  <div class="brand"><span class="brand__dot"></span>TERRAVERA</div>
  <div class="point" style="left:24px;top:73px"><span class="kicker" style="color:var(--sun)">Lorem ipsum</span><p class="copy">Lorem Ipsum is simply dummy text of the printing and typesetting industry. Lorem Ipsum has been the industry's standard dummy text ever since the 1500s</p></div>
  <div class="point point--right" style="left:258px;top:73px"><span class="kicker" style="color:var(--cyan)">Lorem ipsum</span><p class="copy">Lorem Ipsum is simply dummy text of the printing and typesetting industry. Lorem Ipsum has been the industry's standard dummy text ever since the 1500s</p></div>
  <div class="point" style="left:24px;top:167px"><span class="kicker" style="color:var(--blue)">Lorem ipsum</span><p class="copy">Lorem Ipsum is simply dummy text of the printing and typesetting industry. Lorem Ipsum has been the industry's standard dummy text ever since the 1500s</p></div>
  <div class="point point--right" style="left:258px;top:167px"><span class="kicker" style="color:var(--green)">Lorem ipsum</span><p class="copy">Lorem Ipsum is simply dummy text of the printing and typesetting industry. Lorem Ipsum has been the industry's standard dummy text ever since the 1500s</p></div>
  <div class="four__hub"><span></span></div>
</section>

<!-- Table -->
<section class="slide slide--small tablesl">
  <p class="section-label">SECTION NAME HERE</p>
  <h2 class="slide-title">TABLE SLIDE GOES HERE</h2>
  <div class="title-rule"></div>
  <div class="brand"><span class="brand__dot"></span>TERRAVERA</div>
  <table class="data">
    <thead><tr>
      <th style="width:195px;background:var(--blue)">Heading 1</th>
      <th style="width:70px;background:#1a8ad6">Heading 2</th>
      <th style="width:105px;background:var(--sun)">Heading 3</th>
      <th style="width:71px;background:var(--lime)">Heading 4</th>
    </tr></thead>
    <tbody>
      <tr><td>Lorem Ipsum is simply dummy text</td><td>xxx</td><td>Lorem Ipsum</td><td>xxx</td></tr>
      <tr><td>Lorem Ipsum is simply dummy text</td><td>xxx</td><td>Lorem Ipsum</td><td>xxx</td></tr>
      <tr><td>Lorem Ipsum is simply dummy text</td><td>xxx</td><td>Lorem Ipsum</td><td>xxx</td></tr>
      <tr><td>Lorem Ipsum is simply dummy text</td><td>xxx</td><td>Lorem Ipsum</td><td>xxx</td></tr>
      <tr><td>Lorem Ipsum is simply dummy text</td><td>xxx</td><td>Lorem Ipsum</td><td>xxx</td></tr>
      <tr><td>Lorem Ipsum is simply dummy text</td><td>xxx</td><td>Lorem Ipsum</td><td>xxx</td></tr>
      <tr><td>Lorem Ipsum is simply dummy text</td><td>xxx</td><td>Lorem Ipsum</td><td>xxx</td></tr>
      <tr><td>Lorem Ipsum is simply dummy text</td><td>xxx</td><td>Lorem Ipsum</td><td>xxx</td></tr>
      <tr><td>Lorem Ipsum is simply dummy text</td><td>xxx</td><td>Lorem Ipsum</td><td>xxx</td></tr>
      <tr><td>Lorem Ipsum is simply dummy text</td><td>xxx</td><td>Lorem Ipsum</td><td>xxx</td></tr>
    </tbody>
  </table>
</section>

<!-- Timeline -->
<section class="slide slide--small timeline">
  <p class="section-label">SECTION NAME HERE</p>
  <h2 class="slide-title">TIMELINE SLIDE GOES HERE</h2>
  <div class="title-rule"></div>
  <div class="brand"><span class="brand__dot"></span>TERRAVERA</div>
  <div class="tl__line"></div>
  <div class="tl__end" style="left:16px"></div>
  <div class="tl__end" style="left:468px"></div>

  <div class="tl__stem" style="left:64px;top:80px;height:74px"></div>
  <p class="tl__note copy" style="left:72px;top:84px">Lorem Ipsum is simply dummy text of the printing and typesetting industry.</p>
  <div class="tl__stem" style="left:205px;top:80px;height:74px"></div>
  <p class="tl__note copy" style="left:213px;top:84px">Lorem Ipsum is simply dummy text of the printing and typesetting industry.</p>
  <div class="tl__stem" style="left:345px;top:80px;height:74px"></div>
  <p class="tl__note copy" style="left:353px;top:84px">Lorem Ipsum is simply dummy text of the printing and typesetting industry.</p>

  <div class="tl__stem" style="left:135px;top:178px;height:74px"></div>
  <p class="tl__note copy" style="left:143px;top:196px">Lorem Ipsum is simply dummy text of the printing and typesetting industry.</p>
  <div class="tl__stem" style="left:276px;top:178px;height:74px"></div>
  <p class="tl__note copy" style="left:284px;top:196px">Lorem Ipsum is simply dummy text of the printing and typesetting industry.</p>
  <div class="tl__stem" style="left:416px;top:178px;height:74px"></div>
  <p class="tl__note copy" style="left:424px;top:196px">Lorem Ipsum is simply dummy text of the printing and typesetting industry.</p>

  <span class="tl__node" style="left:52px;background:var(--sky)">1</span>
  <span class="tl__node" style="left:123px;background:var(--lime)">2</span>
  <span class="tl__node" style="left:193px;background:var(--sun)">3</span>
  <span class="tl__node" style="left:264px;background:var(--sky)">4</span>
  <span class="tl__node" style="left:334px;background:var(--lime)">5</span>
  <span class="tl__node" style="left:404px;background:var(--sun)">6</span>
</section>

</body>
</html>
```